Flyer for Clothing Line Launch Event

I need a flyer designed for the launch of my women's clothing line in February 2016. I will need to use this flyer on my website, social media and print.

The Collections

Our contemporary collections are comprised of influences drawing from bohemian and chic motifs. The term "Bohemian" is described as "simply an artist or littérateur who, consciously or unconsciously, secedes from conventionality in life and in art". "Chic" was borrowed from the French in the late 19th century and has come to mean stylish or elegant.

About my company:

We design free and romantic garments targeted to fashion-forward women driven by uniqueness and desire to accentuate her confidence and class through style. We look forward to our clients indulging in the LorettaVance brand to include our Keystone Circle, Lend-A-Heart, eNewsletters, Trunk Shows and Fashion Shows.

Target Market(s)

upscale women ages 30-50

Industry/Entity Type

Fashion

Font styles to use
Decorative
Script
Other font styles liked:
• Handwritten type script

Colors
000000
f37122
3377b5
e667a6

Requirements
Must have
• colors similar to my website boutique.lorettavance-example.com
• my logo
Nice to have
• image from my website
• my logo

```html
<!DOCTYPE html>
<html lang="en">
<head>
<meta charset="utf-8">
<title>LorettaVance Boutique – Collection Launch Soirée</title>
<link rel="stylesheet" href="https://fonts.googleapis.com/css2?family=Lato:wght@300;400&family=Parisienne&display=swap">
<style>
  :root {
    --paper: #f7f6f4;
    --band: #3b3b3d;
    --band-edge: #4a4a4c;
    --ink: #3d3d3f;
    --ink-soft: #6e6e70;
    --accent: #e2622b;
    --rule: #b9b8b6;
    --photo-light: #d9dadd;
    --photo-mid: #8d95a8;
    --photo-deep: #3f4f7e;
  }
  * { margin: 0; padding: 0; box-sizing: border-box; }
  html, body { width: 859px; height: 1200px; overflow: hidden; background: var(--paper); }
  .flyer { position: relative; width: 859px; height: 1200px; background: var(--paper); overflow: hidden; }

  .backdrop { position: absolute; inset: 0; width: 859px; height: 1200px; }

  .brand {
    position: absolute; left: 70px; top: 250px; width: 330px;
    text-align: center;
  }
  .brand-mark {
    display: block; width: 46px; height: 46px; margin: 0 auto 14px;
    border-radius: 50%; background: var(--accent);
  }
  .brand-name {
    font-family: "Lato", sans-serif; font-weight: 300;
    font-size: 38px; letter-spacing: 1px; color: var(--ink);
  }

  .details {
    position: absolute; left: 40px; top: 420px; width: 380px;
    text-align: center; color: var(--ink);
  }
  .intro {
    font-family: "Lato", sans-serif; font-weight: 300;
    font-size: 26px; line-height: 1.3;
  }
  .invite {
    margin-top: 22px;
    font-family: "Parisienne", cursive; font-size: 30px; line-height: 1.2;
    color: var(--accent);
  }
  .date {
    margin: 40px auto 0; width: 330px;
    padding: 14px 0;
    border-top: 1px solid var(--rule); border-bottom: 1px solid var(--rule);
    font-family: "Lato", sans-serif; font-weight: 300; font-size: 32px;
  }
  .program {
    list-style: none; margin-top: 46px;
    font-family: "Parisienne", cursive; font-size: 31px; line-height: 1.45;
    color: var(--accent);
  }

  .website {
    position: absolute; right: 48px; bottom: 48px;
    font-family: "Lato", sans-serif; font-weight: 400; font-size: 27px;
    color: var(--accent); letter-spacing: 0.5px;
  }
</style>
</head>
<body>
  <main class="flyer">
    <svg class="backdrop" viewBox="0 0 859 1200" aria-hidden="true">
      <defs>
        <linearGradient id="model-photo-tones" x1="0" y1="0" x2="1" y2="1">
          <stop offset="0" stop-color="var(--photo-light)"/>
          <stop offset="0.45" stop-color="var(--photo-mid)"/>
          <stop offset="1" stop-color="var(--photo-deep)"/>
        </linearGradient>
      </defs>
      <polygon class="top-band" points="0,0 859,0 859,40 0,200" fill="var(--band)"/>
      <polygon class="bottom-band" points="0,955 859,1060 859,1200 0,1200" fill="var(--band)"/>
    </svg>

    <svg class="backdrop" viewBox="0 0 859 1200">
      <polygon class="model-photo" role="img"
        aria-label="Photograph of a model in a long blue tie-dye dress standing beside a pale column"
        points="400,110 859,26 859,1060 400,1009"
        fill="url(#model-photo-tones)"/>
    </svg>

    <header class="brand">
      <span class="brand-mark"></span>
      <div class="brand-name">LorettaVance</div>
    </header>

    <section class="details">
      <p class="intro">Introducing<br>LorettaVance Boutique</p>
      <p class="invite">Please join<br>designer LorettaVance<br>for her Collection Launch Soirée</p>
      <p class="date">February 20, 2016</p>
      <ul class="program">
        <li>Runway Show</li>
        <li>Shopping</li>
        <li>Lite Bites &amp; Champagne</li>
      </ul>
    </section>

    <footer class="website">www.lorettavance-example.com</footer>
  </main>
</body>
</html>
```